BrisaLume Supplement Bottle Label

We need our label redesigned with a fresh spin! :)

I really like bright colors, bright blue, and bright green are the two colors I'd like to use, but want a CLEAN PROFESSIONAL MEDICAL feel overall. Think Zelvan

I see myself as a bridge between science-based medicine and natural medicine and that is also my wish for Brisalume, my supplement brand.

I like the root in the background of the bottle

I also like the new BL symbols below

I am also attaching my book image. I'd like the Brisalume brand to complement my Quiet Current brand :-)
Updates

Project Deadline Extended Reason: We are now guaranteeing the payment to get a design we like :) Added Thursday, May 19, 2016

Still looking for a clean, modern, professional, medical feel :) Added Thursday, May 19, 2016

Industry/Entity Type

Health And Wellness

Font styles to use
Serif
Sans Serif

Requirements
Must have
• Blue- for medical
• Green- for natural
• The word Brisa should be in green, Blue- should be for -Lume.
Nice to have
• I'd like the product labels to convey the brand: vibrant, health restoring, trustworthy, professional. The colorful one we looked at was one I really liked.

```html
<!DOCTYPE html>
<html lang="en">
<head>
<meta charset="utf-8">
<title>BrisaLume Dietary Supplement Label</title>
<link rel="stylesheet" href="https://fonts.googleapis.com/css2?family=Jost:wght@400;500;600&family=Open+Sans+Condensed:wght@300;700&display=swap">
<style>
  :root{
    --bg:#aeeecb;
    --label:#f4f6f7;
    --blue:#1ba8d0;
    --blue-deep:#1a90b8;
    --blue-light:#5fc6e4;
    --green:#a6d21c;
    --green-deep:#8fbd10;
    --root-tint:#cfe4ec;
    --white:#ffffff;
  }
  *{box-sizing:border-box;margin:0;padding:0}
  html,body{width:1200px;height:982px;overflow:hidden}
  body{background:var(--bg);font-family:"Jost",sans-serif;position:relative}
  .label{position:absolute;left:60px;top:210px;width:1080px;height:560px;background:var(--label);
    display:flex;overflow:hidden;box-shadow:0 18px 40px rgba(40,110,90,.18)}
  .panel{position:relative;height:100%;overflow:hidden}
  .panel-front{width:460px}
  .panel-facts{width:330px}
  .panel-directions{width:290px}
  .band{position:absolute;left:0;right:0;top:400px;height:100px;background:var(--blue)}
  .stripes{position:absolute;left:0;right:0;top:500px;height:60px;
    background:linear-gradient(var(--label) 0 14px,var(--blue-light) 14px 24px,var(--label) 24px 34px,var(--blue) 34px 60px)}
  .roots{position:absolute;left:40px;top:20px;width:380px;height:360px;border-radius:50% 50% 40% 40%;
    background:radial-gradient(ellipse at 50% 20%,var(--root-tint),rgba(207,228,236,0) 70%)}
  .brand{position:absolute;top:60px;left:0;right:0;text-align:center;
    font-weight:600;font-size:44px;letter-spacing:2px}
  .brand-first{color:var(--green)}
  .brand-second{color:var(--blue)}
  .brand-ring{position:absolute;top:130px;left:50%;margin-left:-44px;width:88px;height:88px;border:5px solid var(--green);border-radius:50%}
  .product{position:absolute;top:232px;left:0;right:0;text-align:center;color:var(--green);font-weight:500;line-height:1.02}
  .product .line1{font-size:68px;display:block}
  .product .line2{font-size:64px;display:block;margin-top:12px}
  .net-wt{position:absolute;top:418px;left:0;right:0;text-align:center;color:var(--white);font-size:44px;font-weight:400}
  .facts{position:absolute;left:24px;top:40px;width:282px;border:3px solid var(--green);padding:8px 12px 10px;
    font-family:"Open Sans Condensed",sans-serif;background:var(--white)}
  .facts h2{font-family:"Jost",sans-serif;font-weight:400;color:var(--blue);font-size:30px;line-height:1}
  .facts .serving{color:var(--blue-deep);font-size:11px;margin-top:4px;line-height:1.35}
  .facts .head{display:flex;justify-content:space-between;border-top:7px solid var(--green);border-bottom:5px solid var(--green);
    margin-top:6px;padding:4px 0 8px;font-size:11px;font-weight:700;color:var(--blue-deep)}
  .facts .row{display:flex;justify-content:space-between;border-bottom:2px solid var(--green);padding:5px 26px 2px 0;font-size:11px;font-weight:700;color:var(--blue-deep)}
  .facts .row .pct{font-family:"Jost",sans-serif;font-weight:400}
  .facts .end{height:7px;background:var(--green);margin-top:4px}
  .badge{position:absolute;left:24px;top:420px;width:48px;height:60px;background:var(--green);border:3px solid var(--white);
    border-radius:4px 4px 24px 24px}
  .badge-text{position:absolute;left:84px;top:418px;width:236px;color:var(--white);font-family:"Open Sans Condensed",sans-serif;font-size:11px;line-height:1.45}
  .badge-text .web{display:block;margin-top:2px}
  .directions{position:absolute;left:18px;top:40px;width:250px;color:var(--blue-deep);font-family:"Open Sans Condensed",sans-serif;font-size:14px;line-height:1.55}
  .directions strong{font-weight:700}
  .lot{position:absolute;left:18px;top:340px;color:var(--blue-deep);font-family:"Open Sans Condensed",sans-serif;font-weight:700;font-size:12px}
</style>
</head>
<body>
  <main class="label">
    <section class="panel panel-front">
      <div class="band"></div>
      <div class="stripes"></div>
      <div class="roots" role="img" aria-label="Faint pale blue tree roots spreading behind the brand name"></div>
      <h1 class="brand"><span class="brand-first">BRISA</span><span class="brand-second">LUME</span></h1>
      <div class="brand-ring"></div>
      <p class="product"><span class="line1">DIETARY</span><span class="line2">SUPPLEMENT</span></p>
      <p class="net-wt">NET WT.450 G(1 LB)</p>
    </section>

    <section class="panel panel-facts">
      <div class="band"></div>
      <div class="stripes"></div>
      <div class="facts">
        <h2>Supplement Facts</h2>
        <p class="serving">Sed ut perspiciatis unde omnis is<br>sit aspernatur aut</p>
        <div class="head"><span>magni dolore</span><span>quia dolor sit</span></div>
        <div class="row"><span>onsequuntur</span><span class="pct">10%</span></div>
        <div class="row"><span>dolore</span><span class="pct">12%</span></div>
        <div class="row"><span>aut odit aut</span><span class="pct">20%</span></div>
        <div class="row"><span>Neque porro</span><span class="pct">23%</span></div>
        <div class="row"><span>quaerat voluptatem</span><span class="pct">6%</span></div>
        <div class="row"><span>nisi ut aliquid ex</span><span class="pct">8%</span></div>
        <div class="row"><span>Quis autem vel eum</span><span class="pct">12%</span></div>
        <div class="row"><span>consectetur adipiscing</span><span class="pct">41%</span></div>
        <div class="row"><span>labore et dolore</span><span class="pct">30%</span></div>
        <div class="end"></div>
      </div>
      <div class="badge"></div>
      <p class="badge-text">Lorem ipsum dolor sit amet, consectetur adipiscing elit, sed do eiusmod tempor incididunt ut labore et dolore magna aliqua.<span class="web">www.qualitymarks-info.org/gmp</span></p>
    </section>

    <section class="panel panel-directions">
      <div class="band"></div>
      <div class="stripes"></div>
      <p class="directions"><strong>Recommended use:</strong> Take two capsules daily with water and food, or as directed by your healthcare practitioner. Do not exceed the stated dose. Keep out of reach of children. Store in a cool, dry place away from direct sunlight.</p>
      <p class="lot">Lot 115 · Best before: see base</p>
    </section>
  </main>
</body>
</html>
```